Specialty Plumbing Distributor Advertisement Flyer

We are looking to design a flyer to catch the eye of backflow preventer training schools and instructors and advertise a program we have here. Our company specializes in repair parts, tools, technical assistance etc. and through this no-cost program, we donate educational material to assist trainers for their classes. We offer coupons, store credit and free resources on website. It is called our “Keystone Mentor Scheme” and we also have a page on our website dedicated to the trainers we work with, where we send customers of ours that need backflow schooling.
Target Market(s)
Plumbing Training Schools
Industry/Entity Type
Education

```html
<!DOCTYPE html>
<html lang="en">
<head>
<meta charset="utf-8">
<title>Keystone Mentor Scheme Flyer</title>
<link href="https://fonts.googleapis.com/css2?family=Oswald:wght@500;600&family=Lato:wght@400;700&display=swap" rel="stylesheet">
<style>
  :root {
    --page-bg: #e6e6e6;
    --navy: #2b3f86;
    --navy-deep: #1e2d66;
    --blue-glow: #3a55a8;
    --red: #c8161d;
    --red-deep: #9e0f15;
    --silver-light: #f4f4f4;
    --silver: #c9cbce;
    --silver-dark: #8e9096;
    --grey-hero: #8a8c92;
    --grey-hero-dark: #55575d;
    --ink: #2a2a2a;
    --white: #ffffff;
  }
  * { margin: 0; padding: 0; box-sizing: border-box; }
  html, body { width: 1081px; height: 1200px; overflow: hidden; }
  body { background: var(--page-bg); position: relative; }

  .flyer {
    position: absolute; left: 94px; top: 22px;
    width: 850px; height: 1100px;
    transform: scale(1.05); transform-origin: top left;
    background: var(--white);
    box-shadow: 0 6px 18px rgba(0,0,0,.25);
    overflow: hidden;
    font-family: "Lato", sans-serif;
  }

  /* Header */
  .header {
    position: absolute; left: 0; top: 0; width: 850px; height: 122px;
    background: linear-gradient(180deg, var(--silver-light), #dcdde0);
  }
  .brand {
    position: absolute; left: 150px; top: 24px;
    color: var(--navy); font-family: "Lato", sans-serif; font-weight: 400;
  }
  .brand-name { font-size: 44px; line-height: 50px; letter-spacing: .3px; }
  .brand-sub { font-size: 22px; line-height: 24px; }
  .brand-mark {
    position: absolute; left: 60px; top: 40px; width: 44px; height: 44px;
    background: var(--navy);
  }

  /* Hero */
  .hero {
    position: absolute; left: 0; top: 122px; width: 850px; height: 343px;
    background: radial-gradient(ellipse at 30% 40%, var(--grey-hero) 0%, var(--grey-hero-dark) 100%);
  }
  .hero-photo { position: absolute; left: 0; top: 0; }
  .hero-title {
    position: absolute; left: 28px; top: 48px;
    font-family: "Oswald", sans-serif; font-weight: 600;
    color: var(--white); font-size: 54px; line-height: 69px;
    text-transform: uppercase; letter-spacing: .5px;
  }
  .hero-rule {
    position: absolute; left: 33px; top: 263px; width: 212px; height: 4px;
    background: var(--red);
  }
  .hero-program {
    position: absolute; left: 33px; top: 278px;
    font-family: "Oswald", sans-serif; font-weight: 600;
    color: var(--white); font-size: 26px; line-height: 40px; letter-spacing: .3px;
    text-transform: uppercase;
  }
  .silver-rule {
    position: absolute; left: 0; width: 850px; height: 6px;
    background: linear-gradient(90deg, var(--silver-dark), var(--silver-light) 50%, var(--silver-dark));
  }

  /* Info band */
  .info {
    position: absolute; left: 0; top: 470px; width: 850px; height: 300px;
    background: radial-gradient(ellipse at 45% 60%, var(--blue-glow) 0%, var(--navy) 50%, var(--navy-deep) 100%);
    color: var(--white);
  }
  .info-body {
    position: absolute; left: 30px; top: 38px; width: 464px;
    font-size: 15.2px; line-height: 20px; text-align: justify;
  }
  .info-divider {
    position: absolute; left: 513px; top: 42px; width: 1px; height: 236px;
    background: rgba(255,255,255,.7);
  }
  .info-offer {
    position: absolute; left: 530px; top: 80px; width: 300px;
    font-size: 15px; line-height: 20px; font-weight: 700; text-align: center;
  }
  .info-offer p + p { margin-top: 20px; }

  /* Gallery */
  .gallery { position: absolute; left: 0; top: 765px; width: 850px; height: 192px; background: var(--white); }
  .gallery-shot { position: absolute; top: 5px; height: 182px; }
  .shot-one { left: 0; width: 290px; clip-path: polygon(12px 0, 290px 0, 278px 100%, 0 100%); background: linear-gradient(135deg, #8b8f93, #c0582d 55%, #6d6f72); }
  .shot-two { left: 282px; width: 298px; clip-path: polygon(12px 0, 298px 0, 286px 100%, 0 100%); background: linear-gradient(135deg, #b08a52, #5a6a7a 55%, #c9a16a); }
  .shot-three { left: 570px; width: 280px; clip-path: polygon(12px 0, 280px 0, 280px 100%, 0 100%); background: linear-gradient(135deg, #5b5e63, #b9bbbe 50%, #c9662f); }

  /* Footer */
  .footer { position: absolute; left: 0; top: 957px; width: 850px; height: 143px; }
  .footer-shape { position: absolute; left: 0; top: 0; }
  .apply {
    position: absolute; left: 33px; top: 36px;
    font-family: "Oswald", sans-serif; font-weight: 600;
    font-size: 38px; color: var(--ink); letter-spacing: .3px;
  }
  .contact {
    position: absolute; right: 22px; top: 36px; text-align: right;
    font-family: "Oswald", sans-serif; font-weight: 600; color: var(--white);
  }
  .contact-phone { font-size: 36px; line-height: 48px; letter-spacing: .3px; }
  .contact-web { font-size: 22px; line-height: 36px; letter-spacing: .3px; }
</style>
</head>
<body>
  <main class="flyer">
    <header class="header">
      <div class="brand-mark"></div>
      <div class="brand">
        <div class="brand-name">Summit Valve</div>
        <div class="brand-sub">Supply Company</div>
      </div>
    </header>

    <section class="hero">
      <svg class="hero-photo" width="850" height="343" viewBox="0 0 850 343" role="img" aria-label="Two technicians repairing a large grey and red backflow preventer valve">
        <defs>
          <linearGradient id="heroShot" x1="0" y1="0" x2="1" y2="1">
            <stop offset="0" stop-color="#6c6f71"/>
            <stop offset="0.45" stop-color="#3f3a44"/>
            <stop offset="0.8" stop-color="#a63a2c"/>
            <stop offset="1" stop-color="#2d2e33"/>
          </linearGradient>
        </defs>
        <polygon points="445,0 850,0 850,343 445,343" fill="url(#heroShot)"/>
      </svg>
      <h1 class="hero-title">Backflow<br>Preventer<br>Training Schools</h1>
      <div class="hero-rule"></div>
      <p class="hero-program">Keystone Mentor Scheme</p>
    </section>

    <svg style="position:absolute;left:0;top:0" width="850" height="125" viewBox="0 0 850 125" role="img" aria-label="Upper part of technicians working on the valve">
      <defs>
        <linearGradient id="heroTop" x1="0" y1="0" x2="1" y2="1">
          <stop offset="0" stop-color="#7b7e80"/>
          <stop offset="1" stop-color="#3b3741"/>
        </linearGradient>
        <linearGradient id="edgeSilver" x1="0" y1="0" x2="1" y2="0">
          <stop offset="0" stop-color="#8e9096"/>
          <stop offset="1" stop-color="#f4f4f4"/>
        </linearGradient>
      </defs>
      <polygon points="590,35 850,35 850,125 532,125" fill="url(#heroTop)"/>
      <polygon points="583,35 592,35 536,122 527,122" fill="url(#edgeSilver)"/>
    </svg>

    <div class="silver-rule" style="top:463px"></div>

    <section class="info">
      <p class="info-body">Repairing a backflow preventer can be complex and should only be done by a certified backflow technician. When performing a repair, the goal is to return the assembly to the original manufacturer specifications. The first step will always be to conduct a field test on the backflow preventer to determine what level of repair is required. The next step is to troubleshoot the assembly to pinpoint the problem. Most major brands of backflow preventers are designed and built to provide decades of service and to be repaired without removing them from the pipeline. The number one cause of failure in backflow preventers is due to the dirt and debris that flows through the pipeline. The check valve will foul when the debris gets caught between the disc and seat.</p>
      <div class="info-divider"></div>
      <div class="info-offer">
        <p>Our company specializes in repair parts, tools, technical assistance etc. and through this no-cost program, we donate educational material to assist trainers for their classes.</p>
        <p>We offer coupons, store credit and free resources on website.</p>
      </div>
    </section>

    <section class="gallery">
      <div class="gallery-shot shot-one" role="img" aria-label="Close-up of a check valve being serviced in an orange valve body"></div>
      <div class="gallery-shot shot-two" role="img" aria-label="Hands assembling brass backflow preventer fittings"></div>
      <div class="gallery-shot shot-three" role="img" aria-label="Hand reaching inside an open stainless valve housing"></div>
    </section>

    <footer class="footer">
      <svg class="footer-shape" width="850" height="143" viewBox="0 0 850 143">
        <defs>
          <linearGradient id="footerRed" x1="0" y1="0" x2="1" y2="0">
            <stop offset="0" stop-color="#9e0f15"/>
            <stop offset="0.5" stop-color="#c8161d"/>
            <stop offset="1" stop-color="#a80f16"/>
          </linearGradient>
          <linearGradient id="footerSilver" x1="0" y1="0" x2="1" y2="0">
            <stop offset="0" stop-color="#8e9096"/>
            <stop offset="1" stop-color="#e6e7e9"/>
          </linearGradient>
        </defs>
        <rect x="0" y="0" width="850" height="143" fill="#ffffff"/>
        <polygon points="300,14 850,14 850,22 294,22" fill="url(#footerSilver)"/>
        <polygon points="0,98 260,98 262,106 0,106" fill="url(#footerSilver)"/>
        <polygon points="306,22 850,22 850,143 0,143 0,106 262,106" fill="url(#footerRed)"/>
        <polygon points="300,14 310,14 266,106 256,106" fill="url(#footerSilver)"/>
      </svg>
      <div class="apply">APPLY TODAY!</div>
      <div class="contact">
        <div class="contact-phone">CONTACT US: (800) 555-0142</div>
        <div class="contact-web">WWW.SUMMITVALVEPARTS.COM</div>
      </div>
    </footer>
  </main>
</body>
</html>
```